Vell-Stackers web design

We need a homepage web design with final files to be provided in PSD for a company based in Brisbane called 'Vell-Stackers'. They provide innovative and reliable contract packaging solutions for local and national outsourcing buisnesses.

They have an existing website www.vell-stackers-example.com.au that is in dire need of an update to look more professional and sleek.

Target Market(s)

Engineers, Architects

Industry/Entity Type

Construction

Number of Pages Required

1 page

Requirements
Must have
• Main Navigation
• o Home
• o About Us
• o Spacers
• - Standard Cage Wheel Spacer
• - Heavy Duty Cage Wheel Spacer
• - Pile Cage Foot
• - PreCast Piles
• o Packaging
• o Injection Moulding
• o News
• o Contact Us
• - Client wants an updated more professional look and feel that aligns with their branding.
• - Client likes the use of displaying Products on every page eg www.gravelbrace-example.com that has an image of the product and its name obviously looking better than this.
• The following elements are to be included in the Homepage design concept:
• - Room for a Flash banner of rotating images
• - Horizontal navigation (can you show how drop down will appear as well)
• - Logo is attached
• - Phone number needs to appear prominently on every page 07 5918 4607
• - Use Arial font throughout concept incl logo
• - Intro text on page somewhere
• - Products need to be listed on page somewhere there are 7 products (image and name with click through)
• - 2 containers/icons to highlight areas on site Latest News and Contact Us
• - Images – have attached a few that can be used in concepts and also below are some pixquarry images that could be used in banner:
• http://www.pixquarry-example.com/stock-photo-4826153-several-paint-buckets.php
• http://www.pixquarry-example.com/stock-photo-3158207-cans-of-paint.php
• http://www.pixquarry-example.com/stock-photo-8047391-reinforcing-steel.php
• http://www.pixquarry-example.com/stock-photo-2693845-huge-bridge-pier.php
• http://www.pixquarry-example.com/stock-photo-9381427-highway-bridge.php
• http://www.pixquarry-example.com/stock-photo-1470638-bridge.php
• http://www.pixquarry-example.com/stock-photo-6205914-bridge-to-nowhere-yet.php

```html
<!DOCTYPE html>
<html lang="en">
<head>
<meta charset="utf-8">
<title>Vell-Stackers – Home</title>
<link href="https://fonts.googleapis.com/css2?family=Arimo:wght@400;700&display=swap" rel="stylesheet">
<style>
:root{
  --page-bg:#b4b4b4;
  --brand-red:#952427;
  --nav-red:#871b1e;
  --nav-active:#6f1114;
  --drop-bg:#8e3a3d;
  --white:#ffffff;
  --panel:#f3f3f3;
  --intro-bg:#f3f2fb;
  --lilac:#8580c0;
  --tile:#dedede;
  --text:#2b2b2b;
  --link-red:#9a2328;
}
*{margin:0;padding:0;box-sizing:border-box}
html,body{width:933px;height:1200px;overflow:hidden}
body{background:var(--page-bg);font-family:'Arimo',Arial,sans-serif;color:var(--text);position:relative}
.abs{position:absolute}

.site-header{left:44px;top:0;width:849px;height:160px;background:var(--brand-red);border-radius:0 0 18px 18px}
.brand{left:117px;top:22px;display:flex;align-items:center;gap:10px}
.brand-mark{width:42px;height:42px;border-radius:50%;background:#c84a3c}
.brand-name{color:var(--white);font-size:16px;font-weight:700}
.phone{right:68px;top:20px;color:var(--white);font-size:17px;font-weight:700;display:flex;align-items:center;gap:14px}

.main-nav{left:44px;top:107px;width:849px;height:27px;background:var(--nav-red)}
.nav-item{top:0;height:27px;line-height:27px;color:var(--white);font-size:13px;text-align:center}
.nav-item.active{background:var(--nav-active)}
.dropdown{left:283px;top:134px;width:200px}
.dropdown li{list-style:none;height:29px;line-height:28px;padding-left:12px;background:var(--drop-bg);color:var(--white);font-size:12.5px;border-bottom:1px solid #c9a1a2}

.content-panel{left:44px;top:180px;width:849px;height:884px;background:var(--white)}

.banner{left:64px;top:197px;width:583px;height:216px;background:linear-gradient(100deg,#d44a3f 0%,#f4eec0 18%,#f5d64b 35%,#f8f4ea 55%,#ef8a4a 72%,#f6efe9 100%)}
.banner-caption{left:64px;top:341px;width:583px;height:72px;background:rgba(190,110,112,.88)}
.banner-title{left:90px;top:364px;color:var(--white);font-size:27px;letter-spacing:1px}
.banner-more{left:371px;top:375px;color:var(--white);font-size:12px;font-weight:700;text-decoration:underline}

.intro{left:64px;top:424px;width:583px;height:173px;background:var(--intro-bg);padding:20px 32px}
.intro h1{font-size:24px;font-weight:400;color:var(--lilac);letter-spacing:1px;margin-bottom:14px}
.intro p{font-size:14.5px;line-height:19px;margin-bottom:10px;color:#333}

.products{left:64px;top:611px;width:583px;height:429px;background:var(--panel)}
.section-head{display:flex;align-items:center;gap:12px}
.section-icon{width:22px;height:20px;position:relative}
.section-icon::before{content:"";position:absolute;left:0;top:6px;width:13px;height:13px;background:#8a86a8}
.section-icon::after{content:"";position:absolute;left:8px;top:0;width:13px;height:13px;background:#6d6990;opacity:.85}
.products .section-head{position:absolute;left:16px;top:14px;color:var(--link-red);font-size:17px}
.products-rule{left:16px;top:37px;width:549px;height:1px;background:var(--lilac)}
.product-divider{left:289px;top:56px;width:1px;height:322px;background:#8a86a8}
.product-tile{width:231px;height:80px;background:var(--tile);display:flex;align-items:center;justify-content:space-between;padding:0 10px}
.product-tile span{color:var(--link-red);font-size:15px;text-decoration:underline}
.product-thumb{width:58px;height:62px;border-radius:3px}

.newsletter{left:657px;top:197px;width:218px;height:150px;background:var(--brand-red);color:var(--white)}
.newsletter h2{position:absolute;left:12px;top:10px;font-size:18px;font-weight:700;letter-spacing:.3px}
.newsletter-rule{left:18px;top:41px;width:182px;height:1px;background:#c36a6c}
.email-label{left:22px;top:68px;font-size:11px}
.email-input{left:67px;top:65px;width:128px;height:15px;background:var(--white)}
.select-box{left:43px;top:111px;width:95px;height:17px;background:linear-gradient(#fff,#ddd);border:1px solid #888;border-radius:4px;font-size:10px;color:#333;line-height:15px;padding-left:6px}
.select-box::after{content:"";position:absolute;right:0;top:0;width:14px;height:15px;background:#5a7fd0;border-radius:0 3px 3px 0}
.submit-btn{left:143px;top:111px;width:52px;height:17px;background:linear-gradient(#fff,#d8d8d8);border:1px solid #888;border-radius:8px;font-size:10px;color:#333;text-align:center;line-height:15px}

.contact-btn{left:677px;top:381px;width:180px;height:43px;border:2px solid #b2474a;border-radius:6px;background:linear-gradient(#f1f1f1,#c9c9c9);display:flex;align-items:center;justify-content:center;gap:10px;color:var(--brand-red);font-size:16px;font-weight:700;letter-spacing:1.5px}

.news{left:657px;top:463px;width:218px;height:473px;background:var(--panel)}
.news .section-head{position:absolute;left:20px;top:12px;color:var(--link-red);font-size:18px}
.rss{position:absolute;right:20px;top:16px;width:18px;height:18px;background:#f08a24;border-radius:3px}
.news-rule{left:20px;top:40px;width:182px;height:1px;background:var(--lilac)}
.news-item{left:20px;width:182px}
.news-item h3{font-size:11.5px;font-weight:400;color:var(--link-red);line-height:15px;margin-bottom:18px}
.news-item p{font-size:11.5px;line-height:15px;color:#222}

.site-footer{left:44px;top:1064px;width:849px;height:73px;background:var(--brand-red);border-radius:0 0 18px 18px;text-align:center;color:var(--white)}
.footer-links{padding-top:20px;font-size:10.5px}
.footer-links .current{color:#3a0a0b}
.copyright{margin-top:13px;font-size:9.5px}
</style>
</head>
<body>

<header class="site-header abs">
  <div class="brand abs" style="left:73px;top:20px">
    <div class="brand-mark"></div>
    <div class="brand-name">Vell-Stackers</div>
  </div>
  <div class="phone abs">
    <svg width="10" height="16" viewBox="0 0 10 16"><path d="M3 1 L6 1 L5 5 L3 6 Q3 10 6 12 L8 10 L9 14 Q6 16 2 12 Q0 7 3 1Z" fill="#fff"/></svg>
    07 5918 4607
  </div>
</header>

<nav class="main-nav abs">
  <div class="nav-item abs active" style="left:47px;width:96px">Home</div>
  <div class="nav-item abs" style="left:143px;width:88px">About Us</div>
  <div class="nav-item abs active" style="left:239px;width:97px">Spacers</div>
  <div class="nav-item abs" style="left:336px;width:96px">Packaging</div>
  <div class="nav-item abs" style="left:432px;width:128px">Injection Moulding</div>
  <div class="nav-item abs" style="left:565px;width:70px">News</div>
  <div class="nav-item abs" style="left:640px;width:110px">Contact Us</div>
</nav>

<div class="content-panel abs"></div>

<div class="banner abs" role="img" aria-label="Close-up photo of colourful paint buckets"></div>
<div class="banner-caption abs"></div>
<div class="banner-title abs">PLANT UPGRADE -</div>
<div class="banner-more abs">more info</div>

<section class="intro abs">
  <h1>WELCOME TO VSv3!</h1>
  <p>Vell-Stackers Brisbane, providing innovative and reliable contract packaging solutions for local and national outsourcing buisnesses.</p>
  <p>Vell-Stackers Brisbane, providing innovative and reliable contract packaging solutions for local and national outsourcing buisnesses.</p>
</section>

<section class="products abs">
  <div class="section-head"><div class="section-icon"></div>Products</div>
  <div class="products-rule abs"></div>
  <div class="product-divider abs"></div>
  <div class="product-tile abs" style="left:32px;top:58px"><span>Pile Wheel varieties</span><div class="product-thumb" role="img" aria-label="Photo of white cage wheel spacer" style="background:linear-gradient(#f5f5f5,#9a9a9a)"></div></div>
  <div class="product-tile abs" style="left:32px;top:145px"><span>Pile Wheel varieties</span><div class="product-thumb" role="img" aria-label="Photo of brass threaded fittings" style="background:linear-gradient(#e8e2cf,#8a6a2e)"></div></div>
  <div class="product-tile abs" style="left:32px;top:232px"><span>Pile Wheel varieties</span><div class="product-thumb" role="img" aria-label="Photo of coloured plastic discs" style="background:linear-gradient(120deg,#c23a3a,#2f8f5a,#333)"></div></div>
  <div class="product-tile abs" style="left:32px;top:317px"><span>Pile Wheel varieties</span><div class="product-thumb" role="img" aria-label="Photo of metal containers" style="background:linear-gradient(#bdbdbd,#555)"></div></div>
  <div class="product-tile abs" style="left:316px;top:58px"><span>Pile Wheel varieties</span><div class="product-thumb" role="img" aria-label="Photo of black moulded spacers" style="background:linear-gradient(#8a7a6a,#1e1e1e)"></div></div>
  <div class="product-tile abs" style="left:316px;top:145px"><span>Pile Wheel varieties</span><div class="product-thumb" role="img" aria-label="Photo of black heavy duty wheel spacer" style="background:linear-gradient(#666,#111)"></div></div>
  <div class="product-tile abs" style="left:316px;top:232px"><span>Pile Wheel varieties</span><div class="product-thumb" role="img" aria-label="Photo of black pile cage foot" style="background:linear-gradient(#555,#1a1a1a)"></div></div>
</section>

<ul class="dropdown abs">
  <li>Standard Cage Wheel Spacer</li>
  <li>Heavy Duty Cage Wheel Spacer</li>
  <li>Pile Cage Foot</li>
  <li>PreCast Piles</li>
</ul>

<aside class="newsletter abs">
  <h2>Sign up for newsletter</h2>
  <div class="newsletter-rule abs"></div>
  <div class="email-label abs">email :</div>
  <div class="email-input abs"></div>
  <div class="select-box abs">Subscribe</div>
  <div class="submit-btn abs">submit</div>
</aside>

<div class="contact-btn abs">CONTACT US
  <svg width="24" height="16" viewBox="0 0 24 16"><rect x="0.5" y="0.5" width="23" height="15" fill="#fff" stroke="#ccc"/><path d="M1 1 L12 9 L23 1" fill="none" stroke="#bbb"/></svg>
</div>

<aside class="news abs">
  <div class="section-head"><div class="section-icon"></div>Latest News</div>
  <div class="rss"></div>
  <div class="news-rule abs"></div>
  <div class="news-item abs" style="top:65px">
    <h3>1/08/07 || Product News<br>&nbsp;-Spacers Range extended</h3>
    <p>The tooling has now been completed and the Heavy Duty range of easy to fit spacers are now available and in stock...</p>
  </div>
  <div class="news-item abs" style="top:198px">
    <h3>23/08/06 || Product News<br>&nbsp;-New Innovative Spacer</h3>
    <p>We have developed a heavy duty 50mm cover spacer that can be attached to the cage with an 'easy tap' click on fitting...</p>
  </div>
  <div class="news-item abs" style="top:332px">
    <h3>24/07/04 || Product News<br>&nbsp;-PRODUCT IMPROVEMENT</h3>
    <p>The 75mm cover 'Hinged Wheel' spacer has been a very popular product in the concrete pile construction business ...</p>
  </div>
</aside>

<footer class="site-footer abs">
  <div class="footer-links">| <span class="current">Home</span> | About Us | Spacer | Cabins | Packaging | Injection Moulding | News | Contact Us</div>
  <div class="copyright">Copyright @ Vell-Stackers 2009</div>
</footer>

</body>
</html>
```